Graphic Design for Free Community Event

We need a graphic created for a community event that is aimed at families with younger children called Totz Jam. This is a free event and has a fair/carnival feel to it with rides, games, and food. I need the graphic to be flexible enough to be able to be modified and used in a variety of ways on different print and digital marketing materials. I also need the centerpiece of the design to be an event logo that can be used as a standalone element.

The overall feel needs to be fun and friendly with a slightly modern edge to it. Attached are some images used in past events. These are for reference only and do not need to be simulated or used in the final product.

Target Market(s)

Families with children

Industry/Entity Type

Church

Font styles to use
Sans Serif

Requirements
Must have
• - Logo that incorporates the event name- Event Date: August 20 - Event Time: 10am - 2pm - Church name and logo incorporated: Bright Harbor Community Church (see attached logo files)
Nice to have
• - Bright colors- Flexible design elements that are interchangeable and scalable for use of the design in different layouts across different mediums and materials.
Should not have
• - Any references or images related to drugs, alcohol, tobacco, or other subjects that would be inappropriate for children.

```html
<!DOCTYPE html>
<html lang="en">
<head>
<meta charset="utf-8">
<title>Totz Jam – Bright Harbor Community Church</title>
<link rel="stylesheet" href="https://fonts.googleapis.com/css2?family=Fredoka:wght@600;700&family=Montserrat:wght@500&family=Poppins:wght@700;800&display=swap">
<style>
  :root {
    --red: #ec1f2a;
    --yellow: #fbc21b;
    --teal: #2bbcb0;
    --purple: #7b3f94;
    --pink: #e91e63;
    --blush: #f6c3d6;
    --ink: #1c1a1a;
    --cream: #fdf6c6;
    --white: #ffffff;
    --green: #3cb43c;
    --blue: #1f6fd1;
    --orange: #f58220;
    --url: #6a2c91;
  }
  html, body { margin: 0; padding: 0; overflow: hidden; }
  body { width: 810px; height: 1200px; }
  .poster {
    position: relative;
    width: 810px;
    height: 1200px;
    overflow: hidden;
    background: linear-gradient(180deg, var(--cream) 0%, #fffbe8 40%, var(--white) 70%);
    font-family: "Poppins", sans-serif;
  }
  .decor { position: absolute; inset: 0; }

  .church {
    position: absolute;
    top: 58px; left: 0; width: 810px;
    display: flex; align-items: center; justify-content: center; gap: 16px;
  }
  .church-mark {
    width: 104px; height: 104px; border-radius: 50%;
    background: var(--ink);
  }
  .church-name {
    font-family: "Montserrat", sans-serif;
    font-weight: 500;
    color: var(--ink);
    line-height: 1;
    text-transform: uppercase;
  }
  .church-name .primary { display: block; font-size: 38px; letter-spacing: -0.5px; }
  .church-name .secondary { display: block; font-size: 19.5px; margin-top: 5px; letter-spacing: 0.2px; }

  .ribbon { position: absolute; left: 270px; top: 187px; width: 266px; height: 68px; }
  .ribbon-text {
    position: absolute; left: 270px; top: 187px; width: 266px; height: 62px;
    display: flex; align-items: center; justify-content: center;
    font-family: "Poppins", sans-serif; font-weight: 800;
    font-size: 44px; color: var(--white); letter-spacing: 1px;
  }

  .event-title {
    position: absolute; top: 258px; left: 0; width: 810px;
    margin: 0; text-align: center;
    font-family: "Fredoka", sans-serif; font-weight: 700;
    font-size: 134px; line-height: 1; letter-spacing: 1px;
    -webkit-text-stroke: 10px var(--ink);
    paint-order: stroke fill;
    text-shadow: 0 7px 0 var(--ink);
  }
  .event-title .l1 { color: var(--green); }
  .event-title .l2 { color: var(--yellow); }
  .event-title .l3 { color: var(--pink); }
  .event-title .l4 { color: var(--blue); }
  .event-title .l5 { color: var(--purple); }
  .event-title .l6 { color: var(--orange); }
  .event-title .l7 { color: var(--teal); }

  .event-when {
    position: absolute; top: 404px; left: 0; width: 810px;
    margin: 0; text-align: center;
    font-weight: 700; font-size: 51px; letter-spacing: -0.5px;
    color: var(--red);
  }

  .feature-art {
    position: absolute; border-radius: 18px;
    background: rgba(255,255,255,0.22);
  }
  .art-rides { left: 135px; top: 548px; width: 208px; height: 232px; }
  .art-inflatables { left: 490px; top: 578px; width: 184px; height: 166px; }
  .art-food { left: 318px; top: 846px; width: 170px; height: 156px; }

  .feature-label {
    position: absolute; margin: 0;
    font-family: "Fredoka", sans-serif; font-weight: 700;
    color: var(--white); line-height: 1; text-align: center;
    paint-order: stroke fill;
  }
  .label-rides { left: 138px; top: 792px; width: 200px; font-size: 42px; -webkit-text-stroke: 2px #1f8f86; }
  .label-inflatables { left: 452px; top: 764px; width: 260px; font-size: 37px; -webkit-text-stroke: 2px #5a2a70; }
  .label-food { left: 298px; top: 1020px; width: 200px; font-size: 42px; -webkit-text-stroke: 2px #b3141c; }

  .event-link {
    position: absolute; top: 1096px; left: 0; width: 810px;
    margin: 0; text-align: center;
    font-weight: 800; font-size: 34px; letter-spacing: -0.3px;
    color: var(--url);
  }
</style>
</head>
<body>
<main class="poster">
  <svg class="decor" width="810" height="1200" viewBox="0 0 810 1200" aria-hidden="true">
    <g class="confetti">
      <circle cx="60" cy="22" r="9" fill="var(--teal)"/>
      <circle cx="140" cy="14" r="7" fill="var(--yellow)"/>
      <circle cx="215" cy="40" r="11" fill="var(--pink)"/>
      <circle cx="280" cy="12" r="8" fill="var(--teal)"/>
      <circle cx="340" cy="44" r="6" fill="var(--yellow)"/>
      <circle cx="395" cy="18" r="12" fill="var(--teal)"/>
      <circle cx="462" cy="46" r="9" fill="var(--purple)"/>
      <circle cx="520" cy="14" r="7" fill="var(--yellow)"/>
      <circle cx="585" cy="40" r="10" fill="var(--red)"/>
      <circle cx="655" cy="16" r="12" fill="var(--yellow)"/>
      <circle cx="700" cy="52" r="7" fill="var(--pink)"/>
      <circle cx="770" cy="22" r="10" fill="var(--purple)"/>
      <circle cx="30" cy="110" r="14" fill="var(--purple)"/>
      <circle cx="70" cy="78" r="6" fill="var(--red)"/>
      <circle cx="140" cy="95" r="18" fill="var(--teal)"/>
      <circle cx="58" cy="162" r="20" fill="var(--yellow)"/>
      <circle cx="112" cy="150" r="9" fill="var(--pink)"/>
      <circle cx="160" cy="232" r="12" fill="var(--purple)"/>
      <circle cx="25" cy="240" r="7" fill="var(--red)"/>
      <circle cx="222" cy="205" r="14" fill="var(--yellow)"/>
      <circle cx="690" cy="80" r="16" fill="var(--red)"/>
      <circle cx="760" cy="92" r="8" fill="var(--yellow)"/>
      <circle cx="720" cy="140" r="10" fill="var(--teal)"/>
      <circle cx="790" cy="162" r="15" fill="var(--pink)"/>
      <circle cx="662" cy="205" r="22" fill="var(--purple)"/>
      <circle cx="598" cy="242" r="6" fill="var(--yellow)"/>
      <circle cx="752" cy="236" r="9" fill="var(--teal)"/>
      <circle cx="620" cy="110" r="7" fill="none" stroke="var(--pink)" stroke-width="2"/>
      <circle cx="245" cy="150" r="6" fill="none" stroke="var(--teal)" stroke-width="2"/>
      <circle cx="28" cy="352" r="9" fill="var(--yellow)"/>
      <circle cx="788" cy="362" r="8" fill="var(--pink)"/>
      <circle cx="45" cy="472" r="12" fill="var(--pink)"/>
      <circle cx="770" cy="470" r="10" fill="var(--yellow)"/>
      <circle cx="190" cy="495" r="8" fill="var(--teal)"/>
      <circle cx="300" cy="490" r="10" fill="var(--yellow)"/>
      <circle cx="455" cy="508" r="14" fill="var(--teal)"/>
      <circle cx="520" cy="488" r="7" fill="var(--pink)"/>
      <circle cx="600" cy="497" r="16" fill="var(--red)"/>
      <circle cx="762" cy="515" r="18" fill="var(--purple)"/>
      <circle cx="20" cy="640" r="16" fill="var(--yellow)"/>
      <circle cx="790" cy="680" r="14" fill="var(--teal)"/>
      <circle cx="25" cy="790" r="20" fill="var(--red)"/>
      <circle cx="795" cy="800" r="11" fill="var(--yellow)"/>
      <circle cx="40" cy="880" r="14" fill="var(--teal)"/>
      <circle cx="110" cy="900" r="10" fill="var(--yellow)"/>
      <circle cx="185" cy="945" r="22" fill="var(--purple)"/>
      <circle cx="62" cy="982" r="26" fill="var(--pink)"/>
      <circle cx="150" cy="1040" r="12" fill="var(--teal)"/>
      <circle cx="30" cy="1070" r="9" fill="var(--purple)"/>
      <circle cx="210" cy="1078" r="8" fill="var(--red)"/>
      <circle cx="650" cy="890" r="12" fill="var(--yellow)"/>
      <circle cx="740" cy="900" r="24" fill="var(--red)"/>
      <circle cx="612" cy="962" r="16" fill="var(--teal)"/>
      <circle cx="700" cy="992" r="10" fill="var(--pink)"/>
      <circle cx="782" cy="1012" r="18" fill="var(--purple)"/>
      <circle cx="632" cy="1052" r="22" fill="var(--yellow)"/>
      <circle cx="762" cy="1072" r="9" fill="var(--teal)"/>
      <circle cx="40" cy="1172" r="18" fill="var(--teal)"/>
      <circle cx="120" cy="1186" r="10" fill="var(--red)"/>
      <circle cx="250" cy="1165" r="8" fill="var(--purple)"/>
      <circle cx="320" cy="1190" r="14" fill="var(--yellow)"/>
      <circle cx="450" cy="1176" r="10" fill="var(--teal)"/>
      <circle cx="562" cy="1190" r="18" fill="var(--pink)"/>
      <circle cx="650" cy="1166" r="9" fill="var(--purple)"/>
      <circle cx="752" cy="1182" r="20" fill="var(--red)"/>
    </g>
    <g class="streamers">
      <polygon points="95,184 153,198 102,190" fill="var(--orange)"/>
      <polygon points="672,240 692,212 686,238" fill="var(--pink)"/>
      <polygon points="18,284 70,294 25,298" fill="var(--pink)"/>
      <polygon points="715,302 792,295 722,318" fill="var(--orange)"/>
      <polygon points="20,430 67,400 30,438" fill="var(--orange)"/>
      <polygon points="715,402 770,440 760,428" fill="var(--blue)"/>
    </g>
    <g class="feature-discs">
      <circle cx="81" cy="557" r="57" fill="var(--purple)"/>
      <circle cx="413" cy="545" r="34" fill="var(--blush)"/>
      <circle cx="709" cy="574" r="37" fill="var(--yellow)"/>
      <circle cx="412" cy="925" r="170" fill="var(--red)"/>
      <circle cx="238" cy="689" r="178" fill="var(--teal)"/>
      <circle cx="579" cy="701" r="168" fill="var(--purple)"/>
    </g>
  </svg>

  <header class="church">
    <div class="church-mark" aria-hidden="true"></div>
    <div class="church-name">
      <span class="primary">Bright Harbor</span>
      <span class="secondary">Community Church</span>
    </div>
  </header>

  <svg class="ribbon" viewBox="0 0 266 68" aria-hidden="true">
    <polygon points="0,4 266,0 240,30 262,62 6,66 22,34" fill="var(--red)"/>
    <polygon points="6,66 262,62 250,68 14,68" fill="#a8141b"/>
  </svg>
  <div class="ribbon-text">FREE</div>

  <h1 class="event-title"><span class="l1">T</span><span class="l2">O</span><span class="l3">T</span><span class="l4">Z</span> <span class="l5">J</span><span class="l6">A</span><span class="l7">M</span></h1>

  <p class="event-when">August 20 • 10am – 2pm</p>

  <div class="feature-art art-rides" role="img" aria-label="Ferris wheel line icon"></div>
  <div class="feature-art art-inflatables" role="img" aria-label="Bounce house line icon"></div>
  <div class="feature-art art-food" role="img" aria-label="Food truck with burger line icon"></div>

  <p class="feature-label label-rides">RIDES</p>
  <p class="feature-label label-inflatables">INFLATABLES</p>
  <p class="feature-label label-food">FOOD</p>

  <p class="event-link">www.brightharborchurch.org/totzjam</p>
</main>
</body>
</html>
```